Harbor Parcelworks Advertising Flyers

Our logistical company handles purchasing, receiving, and shipment of goods to the Bahamas and we would like to start our marketing and advertising push. The company will also deliver items to clients as well, similar to an Brivora type of experience. We already have our logo designed and we would like to setup our advertising look and feel for our flyers and banner ads. I would like design templates for:
Full Page Flyer: 8.5 in. X 11 in. (width x height) in PDF
Social Media 1: 1080 px x 1350 px (width x height) in JPG or PNG
Social Media 2: 1080 px X 1080 px (width x height) in JPG or PNG
I would like all the PSD files and the information for all fonts used within all the designs as well. I'm sharing our logo and font files for incorporating into the design and for branding.
For design references that we like please review the attached folder with design examples for reference.
The call to action on the flyer/banners should be:
Company Address:
517 NE 46th Lane, Ft. Lauderdale, Florida 33308
Email: Harbor618@mailvane.com
Website: Harbor618.com
We just need them for placeholders and we can add more contact information once the design concepts are confirmed.

Target Market(s)

Persons buying goods online and needing them shipped to them.

Requirements
Must have
• Designs should have strong design elements and be easy to adjust or tweak with copy if necessary.
Nice to have
• I provided examples of designs we like but it doesn't have to be exact.

```html
<!DOCTYPE html>
<html lang="en">
<head>
<meta charset="utf-8">
<title>Harbor Parcelworks Flyer</title>
<link href="https://fonts.googleapis.com/css2?family=Lato:wght@400;500;700&family=Montserrat:wght@600;700&display=swap" rel="stylesheet">
<style>
  :root {
    --navy: #29235c;
    --band-light: #5a5fb8;
    --band-mid: #4447a0;
    --lime: #8cc63f;
    --white: #ffffff;
  }
  html, body { margin: 0; padding: 0; overflow: hidden; background: var(--navy); }
  .flyer {
    position: relative;
    width: 969px;
    height: 1200px;
    overflow: hidden;
    background: var(--navy);
    font-family: "Lato", sans-serif;
    color: var(--white);
  }
  .flyer-shapes { position: absolute; inset: 0; }
  .brand {
    position: absolute;
    left: 612px;
    top: 400px;
    display: flex;
    align-items: center;
    gap: 14px;
  }
  .brand-dot { width: 46px; height: 46px; border-radius: 50%; background: var(--lime); }
  .brand-name {
    font-family: "Montserrat", sans-serif;
    font-weight: 600;
    color: var(--white);
    line-height: 1.05;
    letter-spacing: 1px;
  }
  .brand-name .line-1 { display: block; font-size: 38px; }
  .brand-name .line-2 { display: block; font-size: 17px; letter-spacing: 5px; }
  .headline {
    position: absolute;
    right: 51px;
    top: 508px;
    margin: 0;
    text-align: right;
    font-family: "Montserrat", sans-serif;
    font-weight: 700;
    font-size: 73px;
    line-height: 82px;
    letter-spacing: -0.5px;
  }
  .about { position: absolute; left: 61px; top: 760px; width: 640px; }
  .about-title { margin: 0 0 10px; font-weight: 400; font-size: 48px; line-height: 60px; }
  .about-text { margin: 0 0 22px; font-size: 16.5px; line-height: 22px; }
  .address-block { position: absolute; left: 58px; top: 1030px; }
  .address-row { display: flex; align-items: center; gap: 20px; margin-bottom: 12px; }
  .address-row svg { width: 38px; height: 38px; flex: none; }
  .address-text { font-weight: 500; font-size: 17px; line-height: 22px; }
  .contact { position: absolute; right: 48px; top: 1040px; text-align: right; }
  .contact-label { font-size: 40px; line-height: 48px; }
  .contact-phone { font-weight: 700; font-size: 40px; line-height: 48px; }
  .phone-icon { position: absolute; left: 826px; top: 928px; width: 96px; height: 96px; }
</style>
</head>
<body>
<div class="flyer">
  <svg class="flyer-shapes" width="969" height="1200" viewBox="0 0 969 1200">
    <defs>
      <linearGradient id="heroTone" x1="0" y1="0" x2="0" y2="1">
        <stop offset="0" stop-color="#e9a567"/>
        <stop offset="0.35" stop-color="#d79a72"/>
        <stop offset="0.6" stop-color="#5d6278"/>
        <stop offset="1" stop-color="#4a4f5e"/>
      </linearGradient>
      <linearGradient id="yardTone" x1="0" y1="0" x2="0" y2="1">
        <stop offset="0" stop-color="#c9d6e6"/>
        <stop offset="0.45" stop-color="#b84a44"/>
        <stop offset="0.7" stop-color="#3f7a9a"/>
        <stop offset="1" stop-color="#d8dde4"/>
      </linearGradient>
    </defs>
    <path role="img" aria-label="Photo of a container truck at a port with a cargo ship and an airplane at sunset"
          fill="url(#heroTone)"
          d="M0 0 H890 C650 90 400 330 288 700 L210 560 L0 418 Z"/>
    <path fill="var(--band-light)" opacity="0.75"
          d="M890 0 H969 V30 C680 150 420 400 288 700 C360 400 600 120 890 0 Z"/>
    <path fill="var(--band-mid)" opacity="0.85"
          d="M969 80 V115 C700 220 450 420 300 690 C420 420 680 200 969 80 Z"/>
    <circle cx="122" cy="567" r="156" fill="var(--white)"/>
    <circle role="img" aria-label="Photo of stacked shipping containers with a harbour crane"
            cx="122" cy="567" r="148" fill="url(#yardTone)"/>
    <path fill="var(--lime)" d="M535 1200 C610 1000 790 870 969 852 V1200 Z"/>
  </svg>

  <div class="brand">
    <span class="brand-dot"></span>
    <span class="brand-name"><span class="line-1">HARBOR</span><span class="line-2">PARCELWORKS</span></span>
  </div>

  <h1 class="headline">Lorem<br>ipsum dolor<br>sit amet</h1>

  <section class="about">
    <h2 class="about-title">About Us</h2>
    <p class="about-text">Lorem ipsum dolor sit amet, consectetuer adipiscing elit, sed diam nonum-<br>my nibh euismod tincidunt ut laoreet dolore magna aliquam erat volutpat.<br>Ut wisi enim ad minim veniam. Lorem ipsum dolor sit amet.</p>
    <p class="about-text">Ut nam quas decore maiorum, has te solet affert, ius cu meis quaerendum.<br>Tota possit animal mei te, et nec illud fabellas interpretaris.</p>
  </section>

  <div class="address-block">
    <div class="address-row">
      <svg viewBox="0 0 40 40" fill="none" stroke="#fff" stroke-width="2">
        <path d="M6 36 L9 20 A14 14 0 1 1 22 33 Z"/>
        <circle cx="22" cy="17" r="4"/>
      </svg>
      <div class="address-text">Your first address line<br>Your second address line</div>
    </div>
    <div class="address-row">
      <svg viewBox="0 0 40 40" fill="none" stroke="#fff" stroke-width="2">
        <circle cx="24" cy="15" r="11"/>
        <path d="M16 23 L5 34 L8 37 L19 26"/>
      </svg>
      <div class="address-text">COMPANYNAME.COM</div>
    </div>
  </div>

  <svg class="phone-icon" viewBox="0 0 100 100" fill="none" stroke="#fff" stroke-width="3" stroke-linejoin="round">
    <path d="M78 8 L92 22 C98 28 96 40 86 52 L52 86 C40 96 28 98 22 92 L10 80 L24 66 L36 76 L76 36 L66 24 Z"/>
    <path d="M30 10 L12 28 M42 14 L16 40"/>
  </svg>

  <div class="contact">
    <div class="contact-label">Contact Us</div>
    <div class="contact-phone">012 - 345-6789</div>
  </div>
</div>
</body>
</html>
```